Label for Gin Bottle - Cranberry & Peach

Hi, We have created a Cranberry & Peach Gin that we require a label for.
The gin will be a vivid Orange/red colour in a clear 50cl bottle
The gin will be 40% Vol.
I am looking for a classy design with a summer/fresh appearance.
Thank You.

```html
<!DOCTYPE html>
<html lang="en">
<head>
<meta charset="utf-8">
<title>Cranberry &amp; Peach Gin – Label</title>
<link rel="stylesheet" href="https://fonts.googleapis.com/css2?family=EB+Garamond:wght@400;500&family=Arimo:wght@400&display=swap">
<style>
  :root {
    --canvas-bg: #f1ede8;
    --label-bg: #ffffff;
    --label-edge: #d6d6d6;
    --label-frame: #bdbdbd;
    --ink-dark: #4d4d4f;
    --ink-title: #5a5a5c;
    --ink-small: #777779;
    --fruit-red: #d8283f;
    --fruit-peach: #f39a78;
    --fruit-orange: #ea6a44;
    --leaf-green: #9fd39a;
  }

  html, body {
    margin: 0;
    padding: 0;
    width: 667px;
    height: 1200px;
    overflow: hidden;
    background: var(--canvas-bg);
  }

  .canvas {
    position: relative;
    width: 667px;
    height: 1200px;
  }

  .label {
    position: absolute;
    left: 53px;
    top: 238px;
    width: 560px;
    height: 723px;
    box-sizing: border-box;
    background: var(--label-bg);
    border: 2px solid var(--label-edge);
    border-radius: 10px;
    box-shadow: 0 2px 10px rgba(0, 0, 0, 0.06);
  }

  .label__frame {
    position: absolute;
    inset: 6px;
    border: 2px solid var(--label-frame);
    border-radius: 8px;
  }

  .title {
    position: absolute;
    left: 0;
    right: 0;
    top: 140px;
    margin: 0;
    text-align: center;
    font-family: "EB Garamond", Georgia, serif;
    font-weight: 400;
    font-size: 68px;
    line-height: 1.05;
    color: var(--ink-title);
  }

  .title__line {
    display: block;
    white-space: nowrap;
  }

  .fruit-art {
    position: absolute;
    left: 130px;
    top: 360px;
    width: 296px;
    height: 100px;
    border-radius: 50px;
    background: linear-gradient(90deg,
      var(--leaf-green) 0%,
      var(--fruit-red) 22%,
      var(--fruit-peach) 48%,
      var(--fruit-orange) 70%,
      var(--fruit-red) 88%,
      var(--leaf-green) 100%);
    opacity: 0.85;
  }

  .product-type {
    position: absolute;
    left: 0;
    right: 0;
    top: 520px;
    margin: 0;
    text-align: center;
    font-family: "EB Garamond", Georgia, serif;
    font-weight: 500;
    font-size: 86px;
    letter-spacing: 22px;
    text-indent: 22px;
    line-height: 1;
    color: var(--ink-dark);
  }

  .spec {
    position: absolute;
    top: 666px;
    margin: 0;
    font-family: "Arimo", Arial, sans-serif;
    font-size: 22px;
    line-height: 1;
    color: var(--ink-small);
  }

  .spec--abv { left: 32px; }
  .spec--volume { right: 36px; }
</style>
</head>
<body>
<main class="canvas">
  <section class="label" aria-label="Cranberry and Peach Gin label">
    <div class="label__frame"></div>

    <h1 class="title">
      <span class="title__line">Cranberry</span>
      <span class="title__line">&amp; Peach</span>
    </h1>

    <div class="fruit-art" role="img" aria-label="Illustration of cranberries and a sliced peach with green leaves"></div>

    <p class="product-type">GIN</p>

    <p class="spec spec--abv">40% Vol</p>
    <p class="spec spec--volume">50cl</p>
  </section>
</main>
</body>
</html>
```